Our Company is Harbourline Lotworks and we service the whole Perth Metro region. We want our flyer to grab the potential clients attention and inform them of their potential opportunity to subdivide their residential property. We would like the flyer to show our logo, contact details website and maybe one eye catching, engaging picture/photo. If the Flyer could follow the same colours as our logo that would be great. Are we able to have a A5 size flyer front and back? maybe our contact information on the back? and other services that we offer?
A lot of our potential clients aren't aware their house/land is sub dividable, or even know how to do a subdivision. We would like our flyer to educate the average residential home owner of the potential of their property and make the idea of subdividing seem and easy and accessible. Something along the lines of "Looking to Subdivide? Not sure if your property is sub-dividable? Call us now for a obligation free assessment of your property." or maybe "Subdividing you property is easier than you might think..."
We would like to advertise that we offer:-
Free Subdivision feasibility analysis of your property,
Project Management: We offer full Project Management from start to finish ensuring a hassle free subdivision (or something along those lines)-
New title's application
Updates

Target Market(s)

Residential Home owners with the potential to subdivide their property.

Industry/Entity Type

Surveyor

Colors
f78f20
c3c3c3
3176b5

Requirements
Must have
• Simple, clutter free design offering the idea of subdividing as a new, accessible opportunity to the average homeowner.

```html
<!DOCTYPE html>
<html lang="en">
<head>
<meta charset="utf-8">
<title>Harbourline Lotworks – Subdivision Flyer</title>
<link rel="stylesheet" href="https://fonts.googleapis.com/css2?family=Roboto+Condensed:wght@400;700;900&family=Roboto:wght@300;400;700&display=swap">
<style>
  :root{
    --orange:#f78f20;
    --orange-deep:#e9761a;
    --blue:#3176b5;
    --grey:#c3c3c3;
    --charcoal:#3a3d42;
    --ink:#2b2d31;
    --white:#ffffff;
  }
  *{margin:0;padding:0;box-sizing:border-box}
  html,body{width:900px;height:1200px;overflow:hidden;background:#fff}
  .flyer{position:relative;width:900px;height:1200px;overflow:hidden;background:var(--white);font-family:"Roboto",Arial,sans-serif;color:var(--ink)}

  .hero-photo{position:absolute;left:340px;top:0;width:560px;height:440px;background:linear-gradient(160deg,#c9d7e6 0%,#9fb2c4 45%,#6f7f8c 100%)}
  .hero-panel{position:absolute;left:0;top:0;width:360px;height:440px;background:linear-gradient(180deg,var(--orange) 0%,var(--orange-deep) 100%);padding:40px 0 0 40px;font-family:"Roboto Condensed",Arial,sans-serif;font-weight:900;text-transform:uppercase}
  .hero-kicker{color:var(--white);font-size:44px;line-height:1.02}
  .hero-question{color:var(--white);font-size:62px;line-height:1;margin-top:46px}
  .hero-sub{color:var(--ink);font-size:30px;line-height:1.08;margin-top:6px;font-weight:700}
  .swoosh{position:absolute;left:0;top:320px;width:900px;height:160px}

  .brand{position:absolute;left:60px;top:530px;display:flex;align-items:center;gap:14px}
  .brand-dot{width:28px;height:28px;border-radius:50%;background:var(--blue)}
  .brand-name{font-family:"Roboto Condensed",Arial,sans-serif;font-weight:700;font-size:32px;color:var(--blue);line-height:1.05}

  .round-photo{position:absolute;border-radius:50%;border:7px solid var(--white);box-shadow:0 0 0 5px var(--blue)}
  .round-photo.house{left:370px;top:455px;width:190px;height:190px;background:linear-gradient(180deg,#8fb7e0 0%,#c9a57c 60%,#7d8a5a 100%)}
  .round-photo.street{left:600px;top:440px;width:190px;height:190px;background:linear-gradient(180deg,#a6c8ea 0%,#b9745a 55%,#8c8f7a 100%)}

  .tab{position:absolute;left:0;background:var(--blue);color:var(--white);font-family:"Roboto Condensed",Arial,sans-serif;font-weight:700;text-transform:uppercase;border-radius:0 34px 34px 0;display:flex;align-items:center;padding-left:60px}
  .tab.offer{top:660px;width:360px;height:66px;font-size:44px}
  .tab.project{top:880px;width:450px;height:50px;font-size:28px}

  .offer-title{position:absolute;left:60px;top:738px;font-size:62px;line-height:1;color:var(--ink);font-weight:300;white-space:nowrap}
  .offer-title strong{font-weight:700}
  .offer-sub{position:absolute;left:60px;top:808px;font-size:27px;font-weight:300;color:var(--ink);white-space:nowrap}

  .services{position:absolute;left:600px;top:845px;width:300px;height:255px;background:var(--charcoal);padding:78px 0 0 32px}
  .services-tab{position:absolute;left:-40px;top:16px;width:210px;height:48px;background:var(--orange);color:var(--white);border-radius:24px;font-family:"Roboto Condensed",Arial,sans-serif;font-weight:700;font-size:28px;display:flex;align-items:center;padding-left:28px}
  .services-list{list-style:none;color:var(--white);font-size:21px;line-height:1.25}
  .services-list li::before{content:"•";color:var(--orange);margin-right:8px}
  .services-list .cont{padding-left:18px}
  .services-list .cont::before{content:none}

  .project-copy{position:absolute;left:60px;top:950px;width:480px;font-size:24px;line-height:1.32;color:var(--ink)}

  .contact{position:absolute;left:60px;top:1070px;font-size:19px;color:var(--ink);line-height:1.55}
  .contact-row{display:flex;align-items:center;gap:10px}
  .web{position:absolute;left:600px;top:1112px;width:300px;height:38px;background:var(--charcoal);color:var(--white);font-size:17px;display:flex;align-items:center;padding-left:16px;gap:8px;white-space:nowrap}

  .footer-band{position:absolute;left:0;top:1140px;width:900px;height:60px}
</style>
</head>
<body>
<div class="flyer">
  <div class="hero-photo" role="img" aria-label="Photo of a land surveyor in a hard hat with a total station, buildings behind"></div>
  <div class="hero-panel">
    <div class="hero-kicker">Looking to<br>Subdivide</div>
    <div class="hero-question">Not sure</div>
    <div class="hero-sub">If your property<br>is sub-dividable</div>
  </div>

  <svg class="swoosh" viewBox="0 0 900 160" preserveAspectRatio="none" aria-hidden="true">
    <path d="M0 110 C300 150 600 60 900 0 L900 160 L0 160 Z" fill="var(--white)"/>
    <path d="M0 92 C300 135 600 45 900 -10 L900 8 C600 62 300 150 0 110 Z" fill="var(--blue)"/>
    <path d="M0 112 C300 152 600 64 900 8 L900 18 C600 74 300 160 0 122 Z" fill="var(--orange)"/>
  </svg>

  <div class="brand">
    <span class="brand-dot"></span>
    <span class="brand-name">Harbourline<br>Lotworks</span>
  </div>

  <div class="round-photo house" role="img" aria-label="Photo of a single storey brick home"></div>
  <div class="round-photo street" role="img" aria-label="Photo of new subdivided townhouses along a street"></div>

  <div class="tab offer">We offer</div>
  <div class="offer-title"><strong>Free</strong> Subdivision</div>
  <div class="offer-sub">feasibility analysis of your property</div>

  <div class="services">
    <div class="services-tab">SERVICES</div>
    <ul class="services-list">
      <li>Consultancy</li>
      <li>Planning Application</li>
      <li>Survey Work &amp;</li>
      <li class="cont">Project Management</li>
      <li>Strata Conversions</li>
      <li class="cont">&amp; Amalgamations</li>
    </ul>
  </div>

  <div class="tab project">Project Management</div>
  <p class="project-copy">We offer full Project Management from start to finish ensuring a hassle free subdivision.</p>

  <div class="contact">
    <div class="contact-row">
      <svg width="18" height="18" viewBox="0 0 24 24" aria-hidden="true"><path fill="var(--orange)" d="M6.6 10.8a15 15 0 0 0 6.6 6.6l2.2-2.2a1 1 0 0 1 1-.25 11.4 11.4 0 0 0 3.6.57 1 1 0 0 1 1 1V20a1 1 0 0 1-1 1A17 17 0 0 1 3 4a1 1 0 0 1 1-1h3.5a1 1 0 0 1 1 1c0 1.25.2 2.45.57 3.6a1 1 0 0 1-.25 1z"/></svg>
      <span>0400 318 724</span>
    </div>
    <div class="contact-row">
      <svg width="18" height="18" viewBox="0 0 24 24" aria-hidden="true"><path fill="var(--orange)" d="M3 5h18a1 1 0 0 1 1 1v12a1 1 0 0 1-1 1H3a1 1 0 0 1-1-1V6a1 1 0 0 1 1-1zm9 7 8-5H4z"/></svg>
      <span>info@harbourlinelotworks.com</span>
    </div>
  </div>

  <div class="web">
    <svg width="16" height="16" viewBox="0 0 24 24" aria-hidden="true"><path fill="var(--orange)" d="M8 5v14l11-7z"/></svg>
    <span>www.harbourlinelotworks.com</span>
  </div>

  <svg class="footer-band" viewBox="0 0 900 60" preserveAspectRatio="none" aria-hidden="true">
    <path d="M0 60 L0 42 C300 48 600 36 900 18 L900 60 Z" fill="var(--blue)"/>
    <path d="M0 42 C300 48 600 36 900 18 L900 26 C600 44 300 56 0 50 Z" fill="var(--orange)"/>
  </svg>
</div>
</body>
</html>
```